Brightmoor Learning Trifold Flyer

Brightmoor is an award-winning organisation providing dynamic and creative ways for children, young people, adults and families to make positive change and achieve fulfilling lives.
Brightmoor offers a range of learning solutions focussed on supporting and empowering Individuals and organisations that support people with a range of disabilities. We have 3 core areas of the business - Therapy, Support and Learning.
This flyer is focussed on the learning area of our business - Brightmoor offers a range of learning solutions focussed on supporting and empowering Individuals and organisations that support people with a range of disabilities.
For this flyers we are after an a4 colour double sided flyer in either a A4 tri-fold to DL format or A4 bi-fold to A5 format. We are looking for a design that is simple and dynamic whilst keeping in line with our branding.
The winning designs will need to be hi-res and ready for print and also a lower res version suitable to email.
I have attached a number of files to provide further background, including:
• I have attached a word doc of copy for the flyer
• Brand Guidelines
• Logo
• Our clinic flyer recently produced by a ArtPlenty designer for our clinic area of the business. These flyers do not have to be exactly the same as this one but should appear to be from the same organisation although a different service.
Generally we like our designs to be clear and simple.
Please don't hesitate to reach out with any Q's.

```html
<!DOCTYPE html>
<html lang="en">
<head>
<meta charset="utf-8">
<title>Brightmoor Learning Trifold Flyer</title>
<link href="https://fonts.googleapis.com/css2?family=Montserrat:ital,wght@0,300;0,400;0,500;0,600;0,700;1,700&display=swap" rel="stylesheet">
<style>
:root{
  --stage:#303030;
  --paper:#ffffff;
  --teal:#8fa8ac;
  --teal-dark:#6f8a8f;
  --peach:#d6ae99;
  --peach-dark:#c2957e;
  --ink:#3a3a3a;
  --ink-soft:#5a5a5a;
  --white:#ffffff;
}
*{margin:0;padding:0;box-sizing:border-box}
html,body{width:1200px;height:2731px;overflow:hidden;background:var(--stage)}
body{position:relative;font-family:"Montserrat",Arial,sans-serif;color:var(--ink)}
.spread{position:absolute;left:145px;width:910px;height:642px;background:var(--paper);overflow:hidden}
.spread--outside{top:674px}
.spread--inside{top:1414px}
.panel{position:absolute;top:0;width:303.4px;height:642px;overflow:hidden}
.panel--left{left:0}
.panel--mid{left:303.3px}
.panel--right{left:606.6px}
.abs{position:absolute}
.teal-bg{background:var(--teal)}
.peach-bg{background:var(--peach)}
.brand{display:flex;align-items:center;gap:10px;color:var(--ink);font-weight:500;letter-spacing:.5px}
.brand__dot{border-radius:50%;background:var(--teal);flex:none}

/* outside left */
.about-photos{left:14px;top:12px;width:276px;height:312px;background:linear-gradient(135deg,#d4d4d4,#8a8a8a)}
.about__title{left:20px;top:343px;font-size:17px;font-weight:700;color:var(--teal-dark)}
.about__rule{left:20px;top:368px;width:100px;height:1.5px;background:var(--teal)}
.about__body{left:20px;top:380px;width:262px;font-size:12px;line-height:15.2px;font-weight:400;text-align:justify;color:var(--ink-soft)}

/* outside middle */
.logo-card{left:34px;top:28px;width:238px;height:68px;background:var(--white);border-radius:6px;box-shadow:0 3px 0 var(--teal-dark)}
.logo-card .brand{height:100%;justify-content:center;font-size:29px}
.map{left:30px;top:112px;width:244px;height:175px;background:linear-gradient(160deg,#9db3b6,#86a0a4)}
.contact{left:32px;top:372px;font-size:12.4px;line-height:19px;color:var(--white);list-style:none}
.contact li{display:flex;gap:8px;align-items:flex-start}
.contact li::before{content:"";width:8px;height:8px;border-radius:50%;background:var(--peach);margin-top:5px;flex:none}
.badge{top:455px;background:var(--white);opacity:.92}
.badge--square{left:95px;width:42px;height:76px;border-radius:3px}
.badge--round{left:157px;top:463px;width:42px;height:42px;border-radius:50%;background:none;border:2px solid var(--white)}
.platform{left:0;width:303px;top:547px;text-align:center;color:var(--ink);font-size:12px;font-weight:500}
.platform strong{display:block;font-size:14.5px;font-weight:500;color:var(--white);margin-top:1px}
.phone{left:38px;top:583px;width:230px;height:36px;background:var(--peach);border-radius:5px;box-shadow:0 3px 0 var(--peach-dark);display:flex;align-items:center;justify-content:center;gap:9px;color:var(--white);font-weight:700;font-size:23px}

/* outside right */
.cover-logo{left:30px;top:42px}
.cover-logo .brand{font-size:36px}
.cover-rule{left:150px;top:92px;width:120px;height:1.5px;background:var(--teal)}
.tagline{left:18px;top:120px;width:268px;text-align:center;font-size:15.3px;line-height:18.5px;font-weight:600;color:var(--ink)}
.cover-photo{left:0;top:230px;width:304px;height:366px}
.cover-url{left:0;width:303px;top:605px;text-align:center;font-size:14.5px;font-weight:500}

/* inside left */
.testimonial__tag{left:46px;top:36px;width:210px;height:36px;background:var(--peach);border-radius:3px;color:var(--white);font-weight:700;font-size:23px;letter-spacing:.5px;text-align:center;line-height:36px}
.quote-mark{font-size:34px;font-weight:700;color:#d8d8d8;line-height:1}
.testimonial__body{left:20px;top:90px;width:264px;font-size:9.2px;line-height:11.6px;color:var(--ink-soft)}
.testimonial__by{left:20px;top:230px;border-left:3px solid var(--peach);padding-left:7px;font-size:9.6px;line-height:11.5px;color:var(--teal-dark);font-weight:500}
.learn__intro{left:22px;top:348px;width:265px;font-size:11.2px;line-height:11.6px;color:var(--white)}
.learn__intro p+p{margin-top:13px}
.learn__heading{left:22px;top:484px;width:270px;font-size:13.2px;line-height:15px;font-weight:700;color:var(--white)}
.area{top:525px;width:90px;text-align:center;color:var(--white);font-size:10.5px;line-height:12px}
.area svg{display:block;margin:0 auto 10px}

/* inside middle */
.inside-photo{left:0;top:0;width:304px;height:265px}
.solutions__title{left:22px;top:286px;font-size:13.3px;line-height:15px;font-weight:700;color:var(--white)}
.bullet-list{list-style:none;color:var(--white);font-size:10.7px;line-height:13px}
.bullet-list li{display:flex;gap:7px;margin-bottom:7.5px}
.bullet-list li::before{content:"";width:7px;height:7px;flex:none;margin-top:3px;background:var(--teal);transform:rotate(45deg);border-radius:1px}
.solutions__list{left:22px;top:322px;width:265px}
.sectors__title{left:22px;top:510px;font-size:13.3px;line-height:15px;font-weight:700;color:var(--white)}
.sectors__list{left:22px;top:548px;width:270px;display:grid;grid-template-columns:60px 1fr;column-gap:12px}
.sectors__list li{margin-bottom:7px}

/* inside right */
.inside-logo{left:48px;top:32px}
.inside-logo .brand{font-size:31px}
.url-pill{left:62px;top:88px;width:180px;height:18px;border-radius:9px;background:var(--peach);color:var(--ink);font-size:10.2px;text-align:center;line-height:18px;font-weight:500}
.intro{left:32px;top:117px;width:250px;font-size:9.4px;line-height:11.5px;color:var(--ink-soft)}
.value{top:195px;width:84px;text-align:center;font-size:9.4px;line-height:11px;font-weight:500;color:var(--ink)}
.value svg{display:block;margin:0 auto 6px}
.inperson__tag{left:0;top:336px;width:104px;height:36px;background:var(--white);color:var(--teal-dark);font-size:13px;line-height:13px;font-weight:700;padding:5px 0 0 15px;clip-path:polygon(0 0,90% 0,100% 50%,90% 100%,0 100%)}
.inperson__text{left:124px;top:336px;width:170px;font-size:11px;line-height:12px;color:var(--white)}
.calendar{left:28px;top:385px;width:105px;height:65px;background:linear-gradient(135deg,#e9eef0,#b9c9d8 60%,#e2b9a2)}
.bookings{left:150px;top:400px;width:110px;height:18px;background:var(--white);color:var(--teal-dark);font-size:10px;font-weight:700;text-align:center;line-height:18px}
.ticket-name{left:143px;top:422px;width:130px;text-align:center;font-size:22px;font-weight:600;color:var(--white)}
.packages__banner{left:34px;top:482px;width:238px;height:22px;background:var(--white);color:var(--teal-dark);font-size:13px;font-weight:700;font-style:italic;text-align:center;line-height:22px;clip-path:polygon(0 0,100% 0,96% 50%,100% 100%,0 100%,4% 50%)}
.packages__text{left:14px;top:512px;width:276px;text-align:center;font-size:9.3px;line-height:11.2px;color:var(--white)}
</style>
</head>
<body>

<section class="spread spread--outside">
  <div class="panel panel--left">
    <div class="abs about-photos" role="img" aria-label="Black and white photographs of people with disability and their supporters"></div>
    <h2 class="abs about__title">About Brightmoor</h2>
    <div class="abs about__rule"></div>
    <div class="abs about__body">
      <p>Brightmoor is an award-winning organisation and a Purpose Company, providing dynamic and creative ways for children, young people, adults and families to make positive change and achieve fulfilling lives. As a registered CareFund provider, we offer CareFund services for people with high and intensive needs.</p>
      <p>Our team has extensive experience working with mental health issues and complex disability and people who are neurodivergent to live their best lives. We provide quality, evidence-informed services to adults and children with complex needs along with their families and networks.</p>
    </div>
  </div>

  <div class="panel panel--mid teal-bg">
    <div class="abs logo-card"><div class="brand"><span class="brand__dot" style="width:22px;height:22px"></span>Brightmoor</div></div>
    <div class="abs map" role="img" aria-label="Street map showing the Brightmoor location in Northvale"></div>
    <ul class="abs contact">
      <li>Harbourline Building,<br>42 Wattlefield Ave, Northvale VIC 3999</li>
      <li>learning@brightmoor.au</li>
      <li>www.brightmoor.au</li>
    </ul>
    <div class="abs badge badge--square" role="img" aria-label="Quality certification badge"></div>
    <div class="abs badge badge--round" role="img" aria-label="Certification badge"></div>
    <div class="abs platform">Brightmoor eLearning Platform<strong>www.elearning.brightmoor.au</strong></div>
    <div class="abs phone">
      <svg width="18" height="18" viewBox="0 0 18 18" aria-hidden="true"><rect x="5" y="2" width="8" height="14" rx="1.5" fill="none" stroke="#fff" stroke-width="1.6"/><circle cx="9" cy="13.3" r="0.9" fill="#fff"/></svg>
      03 9000 4812
    </div>
  </div>

  <div class="panel panel--right">
    <div class="abs cover-logo"><div class="brand"><span class="brand__dot" style="width:26px;height:26px"></span>Brightmoor</div></div>
    <div class="abs cover-rule"></div>
    <p class="abs tagline">Empowering supporters of people with disability, mental ill-health and people who are neurodivergent through eLearning</p>
    <svg class="abs cover-photo" viewBox="0 0 304 366" preserveAspectRatio="none" role="img" aria-label="Black and white photograph of a support worker and a young man reading a tablet together">
      <defs><linearGradient id="cover" x1="0" y1="0" x2="1" y2="1"><stop offset="0" stop-color="#e4e4e4"/><stop offset=".55" stop-color="#9a9a9a"/><stop offset="1" stop-color="#4a4a4a"/></linearGradient></defs>
      <polygon points="0,38 152,0 304,38 304,350 152,318 0,350" fill="url(#cover)"/>
      <polyline points="0,30 152,-8 304,30" fill="none" stroke="var(--teal)" stroke-width="6"/>
      <polyline points="0,358 152,326 304,358" fill="none" stroke="var(--teal)" stroke-width="6"/>
    </svg>
    <p class="abs cover-url">elearning.brightmoor.au</p>
  </div>
</section>

<section class="spread spread--inside">
  <div class="panel panel--left">
    <svg class="abs" style="left:0;top:0" width="304" height="642" viewBox="0 0 304 642" aria-hidden="true">
      <polygon points="0,274 152,236 304,274 304,642 0,642" fill="var(--peach)"/>
      <polygon points="0,286 152,248 304,286 304,642 0,642" fill="var(--teal)"/>
    </svg>
    <div class="abs testimonial__tag">TESTIMONIAL</div>
    <span class="abs quote-mark" style="left:20px;top:66px">&ldquo;</span>
    <p class="abs testimonial__body">A big thank you for the way you presented the SAFEHOLD Training for our staff team.<br>The training was very informative, delivered very well and not only was it technically well done, but it was also presented with real life scenarios and with some humour for what can sometimes be heavy content.<br>You fostered a safe environment, encouraged all of us, and made us feel like our contribution and our thoughts were valued.<br>I do hope we get to collaborate with you again</p>
    <p class="abs testimonial__by">Operations Manager, Large disability<br>service organisation, Victoria</p>
    <span class="abs quote-mark" style="left:240px;top:224px">&rdquo;</span>
    <div class="abs learn__intro">
      <p>Brightmoor offers a range of learning solutions focussed on supporting and empowering Individuals and organisations that support people with a range of disabilities.</p>
      <p>Our unique breadth and depth of experience across disability, mental ill-health and neurodiversity combined with the voice of lived experience enables our team to provide practical and real world learning experiences.</p>
    </div>
    <h3 class="abs learn__heading">Broadly, our eLearning offering can be grouped into three broad areas:</h3>
    <div class="abs area" style="left:2px">
      <svg width="36" height="36" viewBox="0 0 36 36" aria-hidden="true"><rect width="36" height="36" rx="4" fill="var(--peach)"/><rect x="8" y="9" width="20" height="14" rx="1.5" fill="none" stroke="var(--ink)" stroke-width="1.8"/><line x1="14" y1="27" x2="22" y2="27" stroke="var(--ink)" stroke-width="1.8"/><line x1="18" y1="23" x2="18" y2="27" stroke="var(--ink)" stroke-width="1.8"/></svg>
      eLearning
    </div>
    <div class="abs area" style="left:106px">
      <svg width="36" height="36" viewBox="0 0 36 36" aria-hidden="true"><rect width="36" height="36" rx="4" fill="var(--peach)"/><circle cx="13" cy="13" r="4" fill="var(--ink)"/><circle cx="23" cy="13" r="4" fill="var(--ink)"/><path d="M6 28c0-5 3-8 7-8s7 3 7 8zM16 28c0-5 3-8 7-8s7 3 7 8z" fill="var(--ink)"/></svg>
      Face To<br>Face Training
    </div>
    <div class="abs area" style="left:210px">
      <svg width="36" height="36" viewBox="0 0 36 36" aria-hidden="true"><rect width="36" height="36" rx="4" fill="var(--peach)"/><rect x="10" y="7" width="16" height="22" rx="1.5" fill="none" stroke="var(--ink)" stroke-width="1.8"/><line x1="14" y1="14" x2="22" y2="14" stroke="var(--ink)" stroke-width="1.6"/><line x1="14" y1="19" x2="22" y2="19" stroke="var(--ink)" stroke-width="1.6"/><line x1="14" y1="24" x2="19" y2="24" stroke="var(--ink)" stroke-width="1.6"/></svg>
      Tailored<br>Training<br>Packages
    </div>
  </div>

  <div class="panel panel--mid peach-bg">
    <svg class="abs inside-photo" viewBox="0 0 304 265" preserveAspectRatio="none" role="img" aria-label="Black and white photograph of a group of young people smiling together in front of a mural">
      <defs><linearGradient id="group" x1="0" y1="0" x2="1" y2="1"><stop offset="0" stop-color="#bdbdbd"/><stop offset="1" stop-color="#5e5e5e"/></linearGradient></defs>
      <polygon points="0,0 304,0 304,262 152,232 0,262" fill="url(#group)"/>
      <polyline points="0,262 152,232 304,262" fill="none" stroke="var(--teal)" stroke-width="5"/>
    </svg>
    <h3 class="abs solutions__title">Our training solutions are<br>targeted towards</h3>
    <ul class="abs bullet-list solutions__list">
      <li>Families and carers</li>
      <li>Support workers and direct care workers</li>
      <li>Positive behaviour support practitioners</li>
      <li>Frontline and customer service staff</li>
      <li>Allied health professionals</li>
      <li>Support co-ordinators, case<br>managers and planners</li>
      <li>Others interacting with, and supporting<br>people with a range of disabilities</li>
    </ul>
    <h3 class="abs sectors__title">The sectors<br>we work in include</h3>
    <ul class="abs bullet-list sectors__list">
      <li>Disability</li><li>Mental health &nbsp;&nbsp;Clinical Health</li>
      <li>Justice</li><li>Health &amp; Community Services</li>
      <li>Forensic</li><li>Other &ndash; entities that are striving<br>to be more inclusive</li>
    </ul>
  </div>

  <div class="panel panel--right">
    <svg class="abs" style="left:0;top:0" width="304" height="642" viewBox="0 0 304 642" aria-hidden="true">
      <polygon points="0,278 152,312 304,278 304,642 0,642" fill="var(--teal)"/>
      <polyline points="0,268 152,302 304,268" fill="none" stroke="var(--teal)" stroke-width="4"/>
    </svg>
    <div class="abs inside-logo"><div class="brand"><span class="brand__dot" style="width:22px;height:22px"></span>Brightmoor</div></div>
    <div class="abs url-pill">www.elearning.brightmoor.au</div>
    <p class="abs intro">We are passionate about empowering paid and unpaid supporters of people with disability, mental ill-health and people who are neurodivergent.<br>Our eLearning packages are affordable, accessible, meaningful and enjoyable. They enable learners to easily translate knowledge into practice.</p>
    <div class="abs value" style="left:20px">
      <svg width="26" height="24" viewBox="0 0 26 24" aria-hidden="true"><circle cx="13" cy="8" r="6" fill="none" stroke="var(--teal)" stroke-width="2.4"/><rect x="4" y="17" width="18" height="6" rx="1" fill="var(--teal)"/></svg>
      Our specialist knowledge and skills
    </div>
    <div class="abs value" style="left:110px">
      <svg width="26" height="24" viewBox="0 0 26 24" aria-hidden="true"><circle cx="7" cy="6" r="3.5" fill="var(--peach)"/><circle cx="19" cy="6" r="3.5" fill="var(--peach)"/><circle cx="13" cy="11" r="3.5" fill="var(--peach)"/><path d="M1 22c0-5 3-7 6-7s6 2 6 7zM13 22c0-5 3-7 6-7s6 2 6 7z" fill="var(--peach)"/></svg>
      The voice of lived experience
    </div>
    <div class="abs value" style="left:200px">
      <svg width="26" height="24" viewBox="0 0 26 24" aria-hidden="true"><rect x="2" y="2" width="22" height="20" fill="none" stroke="var(--teal)" stroke-width="2.4"/><circle cx="13" cy="12" r="4" fill="var(--teal)"/></svg>
      Our point of difference
    </div>
    <div class="abs inperson__tag">In Person<br>Training</div>
    <p class="abs inperson__text">In new our purpose fitted training room we offer in person training.</p>
    <div class="abs calendar" role="img" aria-label="Illustration of a person beside a large booking calendar"></div>
    <div class="abs bookings">Bookings via</div>
    <div class="abs ticket-name">TicketHall</div>
    <div class="abs packages__banner">Tailored Training Packages</div>
    <p class="abs packages__text">Brightmoor develops customised virtual or in person training programs for organisations and communities. This enables a learning program tailored to meet organisation specific learning needs. It also creates opportunity for team building, shared learning and collaboration. Brightmoor also offers a broad range of bespoke training packages on a range of topics including positive behaviour support, trauma informed practice, specific types of disabilities and syndromes, person-centred planning and support work.</p>
  </div>
</section>

</body>
</html>
```